Laundry Service Description Tri-Fold Brochure

My laundry business offers a service called "Mellowtide - Wet Cleaning"
I am after a design for a tri fold brochure to hand out to my customers. This will detail the benefits of wet cleaning vs dry cleaning.
I want the brochure to highlight the customer benefits NOT the business benefits.
I have attached the logo of our laundry which should be included
A couple of links here for more information and pdfs are attached:
https://brimleyhollandsupply.com.au/laundry/mellow-tide-wet-cleaning.html
https://www.quorv.co.za/wet-cleaning/
I have attached the design of our laundry window and ideally i want the brochure designed similar

```html
<!DOCTYPE html>
<html lang="en">
<head>
<meta charset="utf-8">
<title>Mellowtide Wet Cleaning – Tri-Fold Brochure</title>
<link href="https://fonts.googleapis.com/css2?family=Lato:wght@400;700;900&family=Roboto:ital,wght@0,300;0,400;0,700;1,900&display=swap" rel="stylesheet">
<style>
:root{
  --blue:#1f90e2;
  --blue-deep:#0d62b8;
  --blue-light:#4fb0f0;
  --ink:#0e1116;
  --charcoal:#2a2d33;
  --grey:#b8b9bc;
  --paper:#ffffff;
  --text:#2f3237;
  --backdrop:#d4d5d7;
}
*{margin:0;padding:0;box-sizing:border-box}
html,body{width:802px;height:1200px;overflow:hidden}
body{background:var(--backdrop);font-family:"Lato",sans-serif;color:var(--text);position:relative}
.spread{position:absolute;left:82px;width:638px;height:497px;background:var(--paper);overflow:hidden}
.spread--outside{top:77px}
.spread--inside{top:626px}
.panel{position:absolute;top:0;height:100%;overflow:hidden}
.panel svg.panel-bg{position:absolute;inset:0;width:100%;height:100%}
.p1{left:0;width:214px}
.p2{left:214px;width:210px}
.p3{left:424px;width:214px}
.abs{position:absolute}
.heading{font-family:"Roboto",sans-serif;font-weight:300;color:var(--blue);font-size:15px;line-height:1.1}
.bullets{list-style:none;font-size:7px;line-height:9.5px}
.bullets li{position:relative;padding-left:10px}
.bullets li::before{content:"";position:absolute;left:1px;top:3.5px;width:3px;height:3px;border-radius:50%;background:var(--ink)}
.bullets--spaced li{margin-bottom:5px}
.body{font-size:7px;line-height:9.4px}
.dots{display:flex;gap:3px;align-items:center;height:3px}
.dots span{height:3px;background:var(--blue)}
.dots .bar{width:48px}
.dots .dot{width:3px}
.dots--white span{background:#fff}
.contact-title{font-family:"Roboto",sans-serif;font-weight:700;font-size:16px;color:var(--ink);letter-spacing:.2px}
.contact-list{list-style:none;font-size:7px;line-height:9.5px;color:var(--ink)}
.contact-list li{position:relative;padding-left:20px;margin-bottom:4px}
.contact-list svg{position:absolute;left:0;top:0;width:8px;height:8px}
.brand{display:flex;align-items:center;gap:6px}
.brand-mark{width:12px;height:12px;border-radius:50%;background:var(--blue)}
.brand-name{font-family:"Lato",sans-serif;font-weight:900;font-size:22px;color:var(--blue);line-height:1}
.brand-sub{font-size:11px;letter-spacing:1.5px;color:var(--charcoal)}
.service-title{font-family:"Roboto",sans-serif;font-style:italic;font-weight:900;font-size:21px;line-height:22px;color:#5a5d62}
.tagline{font-size:10px;color:#4a4d52}
.headline{font-family:"Roboto",sans-serif;font-weight:300;font-size:22px;line-height:23px;color:var(--blue-light)}
.badge-text{font-size:7.5px;font-weight:700;color:#fff;text-align:center;line-height:9px}
.badge-text .tick{display:block;margin:2px auto 0;width:8px;height:8px}
</style>
</head>
<body>

<!-- Outside spread -->
<section class="spread spread--outside">
  <!-- Inside flap -->
  <div class="panel p1">
    <svg class="panel-bg" viewBox="0 0 214 497" preserveAspectRatio="none">
      <defs>
        <linearGradient id="envBlue" x1="0" y1="1" x2="1" y2="0">
          <stop offset="0" stop-color="#0d62b8"/><stop offset="1" stop-color="#2a9cec"/>
        </linearGradient>
      </defs>
      <polygon points="214,283 13,403 13,487 214,487" fill="url(#envBlue)"/>
      <rect x="0" y="487" width="214" height="10" fill="#0e1116"/>
    </svg>
    <h2 class="heading abs" style="left:24px;top:26px">Simple and flexible</h2>
    <ul class="bullets abs" style="left:24px;top:48px;width:172px">
      <li>Wet clean and wash regular laundry using the same equipment</li>
      <li>Wet clean a wide variety of garments</li>
      <li>Clean wool, silk, and other delicates with ease, including viscose, acetate, rayon, angora, cashmere</li>
      <li>Clean Stormweave and Drylume without damaging the membrane or waterproofing</li>
      <li>Clean 70% of leather and suede garments with Mellowtide</li>
      <li>Wet clean fire-proof clothing</li>
    </ul>
    <h2 class="heading abs" style="left:24px;top:180px">Natural and safe cleaning</h2>
    <ul class="bullets abs" style="left:24px;top:203px;width:160px">
      <li>No air or water pollution – the process only uses water and biodegradable detergents</li>
      <li>Safe for people – no adverse health affects on either operators or customers</li>
      <li>Safe for all garments: you can clean any garment with Mellowtide that you would traditionally dry clean</li>
      <li>Compliant to any sustainable standards Ideal for cleaning special items like children's and baby clothing.</li>
    </ul>
    <h3 class="abs" style="right:18px;top:386px;font-family:'Roboto',sans-serif;font-weight:300;font-size:13.5px;color:#fff">Environmentally friendly</h3>
    <div class="dots dots--white abs" style="left:88px;top:407px"><span class="dot"></span><span class="dot"></span><span class="dot"></span></div>
    <p class="body abs" style="right:18px;top:416px;width:186px;text-align:right;color:#fff;font-size:6.8px;line-height:9.5px">There's a lot to be excited about with Mellowtide, the professional cleaning solution that not only enables you to grow your business in a sustainable way but also helps to protect the environment, your employees and yourself. This is because it uses the earth's most natural solvent, water, and uses it sparingly.</p>
  </div>

  <!-- Back panel -->
  <div class="panel p2">
    <svg class="panel-bg" viewBox="0 0 210 497" preserveAspectRatio="none">
      <defs>
        <linearGradient id="rackPhoto" x1="0" y1="0" x2="1" y2="1">
          <stop offset="0" stop-color="#3c4654"/><stop offset=".6" stop-color="#56657a"/><stop offset="1" stop-color="#232a33"/>
        </linearGradient>
        <linearGradient id="jacketPhoto" x1="0" y1="0" x2="0" y2="1">
          <stop offset="0" stop-color="#4a6f9a"/><stop offset="1" stop-color="#1b3556"/>
        </linearGradient>
      </defs>
      <rect x="0" y="0" width="210" height="300" fill="url(#rackPhoto)" role="img" aria-label="Photo of freshly cleaned shirts hanging on a rail"/>
      <polygon points="0,150 210,270 210,300 0,300" fill="#0e1116"/>
      <g stroke="#0e1116" stroke-width="5">
        <line x1="0" y1="185" x2="95" y2="125"/>
        <line x1="0" y1="200" x2="110" y2="132"/>
        <line x1="0" y1="215" x2="125" y2="139"/>
        <line x1="0" y1="230" x2="140" y2="146"/>
        <line x1="0" y1="245" x2="155" y2="153"/>
      </g>
      <rect x="0" y="290" width="210" height="207" fill="#b8b9bc"/>
      <polygon points="104,203 180,245 180,329 104,371 28,329 28,245" fill="#1f90e2"/>
      <polygon points="104,213 172,250 172,324 104,361 36,324 36,250" fill="url(#jacketPhoto)" role="img" aria-label="Photo of jackets on hangers"/>
    </svg>
    <h2 class="contact-title abs" style="left:38px;top:390px">CONTACT US</h2>
    <ul class="contact-list abs" style="left:38px;top:414px;width:170px">
      <li><svg viewBox="0 0 10 10"><path d="M2 1l2 2-1 1.3c.6 1.2 1.5 2.1 2.7 2.7L7 6l2 2-1.3 1.3C4.5 9 1 5.5.7 2.3z" fill="none" stroke="#0e1116" stroke-width=".8"/></svg>000 123 456 789</li>
      <li style="margin-bottom:0"><svg viewBox="0 0 10 10"><circle cx="5" cy="5" r="4" fill="none" stroke="#0e1116" stroke-width=".8"/><ellipse cx="5" cy="5" rx="1.8" ry="4" fill="none" stroke="#0e1116" stroke-width=".7"/><line x1="1" y1="5" x2="9" y2="5" stroke="#0e1116" stroke-width=".7"/></svg>www.websiteurl.com</li>
      <li>company@domain.com</li>
      <li><svg viewBox="0 0 10 10"><path d="M5 9.5C3 7 2 5.5 2 4a3 3 0 016 0c0 1.5-1 3-3 5.5z" fill="none" stroke="#0e1116" stroke-width=".8"/><circle cx="5" cy="4" r="1" fill="#0e1116"/></svg>Your Address, Office Location,<br>Street Name, Country 4545</li>
    </ul>
  </div>

  <!-- Cover -->
  <div class="panel p3">
    <svg class="panel-bg" viewBox="0 0 214 497" preserveAspectRatio="none">
      <defs>
        <linearGradient id="suitPhoto" x1="0" y1="0" x2="1" y2="0">
          <stop offset="0" stop-color="#8fc3ea"/><stop offset=".45" stop-color="#2c3446"/><stop offset="1" stop-color="#141922"/>
        </linearGradient>
      </defs>
      <rect x="0" y="0" width="214" height="150" fill="#0e1116"/>
      <polygon points="0,90 175,0 214,0 214,22 0,132" fill="#1f90e2"/>
      <polygon points="4,120 214,14 214,262 120,282 4,232" fill="url(#suitPhoto)" role="img" aria-label="Photo of a man in a dark suit in front of a rail of shirts"/>
      <polygon points="0,232 0,250 120,296 214,270 214,262 120,282" fill="#1f90e2"/>
      <rect x="0" y="484" width="214" height="13" fill="#1f90e2"/>
    </svg>
    <div class="abs" style="left:26px;top:348px">
      <div class="brand"><span class="brand-name">Brightwell</span><span class="brand-mark"></span></div>
      <div class="brand-sub" style="margin-top:3px">Laundry Services</div>
    </div>
    <div class="dots abs" style="left:26px;top:397px"><span class="bar" style="width:34px"></span><span class="dot"></span><span class="dot"></span></div>
    <h1 class="service-title abs" style="left:26px;top:405px">Mellowtide<br>Wet Cleaning</h1>
    <div class="dots abs" style="left:120px;top:453px"><span class="bar" style="width:34px"></span><span class="dot"></span><span class="dot"></span></div>
    <p class="tagline abs" style="left:26px;top:463px">Mellowtide Incredibly efficient</p>
  </div>
</section>

<!-- Inside spread -->
<section class="spread spread--inside">
  <div class="panel p1">
    <svg class="panel-bg" viewBox="0 0 214 498" preserveAspectRatio="none">
      <defs>
        <linearGradient id="hangerPhoto" x1="0" y1="0" x2="1" y2="1">
          <stop offset="0" stop-color="#d9dde2"/><stop offset=".5" stop-color="#8aa7c6"/><stop offset="1" stop-color="#3d5f86"/>
        </linearGradient>
        <linearGradient id="bandBlue" x1="0" y1="0" x2="1" y2="0">
          <stop offset="0" stop-color="#0d62b8"/><stop offset="1" stop-color="#2a9cec"/>
        </linearGradient>
      </defs>
      <rect width="214" height="498" fill="#0e1116"/>
      <polygon points="0,0 214,0 214,170 120,225 0,135" fill="url(#hangerPhoto)" role="img" aria-label="Photo of a hand holding a cleaned shirt on a hanger in a protective bag"/>
      <polygon points="0,105 120,195 214,140 214,175 120,230 0,150" fill="url(#bandBlue)"/>
      <polygon points="0,180 70,225 0,230" fill="#1f90e2"/>
      <g stroke="#0e1116" stroke-width="4">
        <line x1="0" y1="155" x2="60" y2="200"/>
        <line x1="0" y1="166" x2="52" y2="205"/>
        <line x1="0" y1="177" x2="44" y2="210"/>
      </g>
    </svg>
    <h2 class="headline abs" style="left:24px;top:250px">Mellowtide<br>cleans 100%<br>of garments,<br>100% of the time.</h2>
    <h3 class="abs" style="left:24px;top:362px;font-size:11px;font-weight:400;color:#fff">What is Mellowtide?</h3>
    <p class="body abs" style="left:24px;top:384px;width:178px;color:#fff">Mellowtide is a new alternative to dry cleaning that is now available. Mellowtide by Veltro is a dry-to-dry wet cleaning process that has been developed and tested in Europe over the past 10 years. It is an environmentally friendly, water based garment care system that has been through extensive testing with all fabric types to ensure it is state of the art and a level above traditional wet cleaning.</p>
  </div>

  <div class="panel p2">
    <svg class="panel-bg" viewBox="0 0 210 498" preserveAspectRatio="none">
      <defs>
        <linearGradient id="towelPhoto" x1="0" y1="0" x2="0" y2="1">
          <stop offset="0" stop-color="#b9d6e6"/><stop offset=".5" stop-color="#5a85ad"/><stop offset="1" stop-color="#5aaab7"/>
        </linearGradient>
      </defs>
      <rect width="210" height="498" fill="#fff"/>
      <polygon points="0,252 210,205 210,240 0,292" fill="#1f90e2"/>
      <polygon points="0,292 210,240 210,498 0,498" fill="#0e1116"/>
      <polygon points="14,385 100,335 200,335 200,498 14,498" fill="url(#towelPhoto)" role="img" aria-label="Photo of a stack of folded towels on a stool"/>
    </svg>
    <h2 class="abs" style="left:20px;top:20px;font-family:'Roboto',sans-serif;font-weight:300;font-size:14px;line-height:18px;color:var(--ink)">What makes up a<br>Mellowtide system?</h2>
    <div class="dots abs" style="left:20px;top:60px"><span class="bar" style="width:50px"></span><span class="dot"></span><span class="dot"></span><span class="dot"></span></div>
    <p class="abs" style="left:20px;top:72px;font-size:8.5px;color:var(--blue)">There are 4 elements:</p>
    <ul class="bullets bullets--spaced abs" style="left:20px;top:89px;width:166px">
      <li>a Veltro washer and dryer</li>
      <li>factory developed Mellowtide programming for the washer and dryer</li>
      <li>Mellowtide detergents including specialised spotting agents for all stain types and a detergent feed system</li>
      <li>finishing or ironing equipment (the system can be used with existing finishing and ironing equipment to save you money)</li>
    </ul>
    <p class="body abs" style="left:20px;top:203px;width:166px">We can supply all washing, drying, ironing and finishing equipment to complete the process. Enquire with us today.</p>
  </div>

  <div class="panel p3">
    <svg class="panel-bg" viewBox="0 0 214 498" preserveAspectRatio="none">
      <defs>
        <linearGradient id="paperFade" x1="0" y1="0" x2="1" y2="0">
          <stop offset="0" stop-color="#e9eaec"/><stop offset=".25" stop-color="#fff"/>
        </linearGradient>
      </defs>
      <rect width="214" height="498" fill="url(#paperFade)"/>
      <polygon points="0,418 214,365 214,498 0,498" fill="url(#bandBlue)"/>
      <polygon points="102,376 150,403 150,457 102,484 54,457 54,403" fill="#fff"/>
      <polygon points="102,382 145,406 145,454 102,478 59,454 59,406" fill="#1f90e2"/>
    </svg>
    <h2 class="abs" style="left:16px;top:28px;font-family:'Roboto',sans-serif;font-weight:400;font-size:13.5px;color:var(--ink)">Why is Mellowtide so unique?</h2>
    <div class="dots abs" style="left:16px;top:52px"><span class="bar" style="width:50px"></span><span class="dot"></span><span class="dot"></span><span class="dot"></span></div>
    <div class="body abs" style="left:16px;top:64px;width:182px">
      <p>Mellowtide is proven to clean 100% of garments, 100% of the time. This includes silk garments which keep their shape and colour beautifully when cleaned using a Mellowtide system, leather jackets, household textiles, furniture coverings and fire-proof garments.</p>
      <p style="margin-top:9px">Oil and grease stains are also no problem for a Mellowtide system which offers superior stain removal, even on the most delicate of fabrics. The Mellowtide spotting chemicals help remove all types of stains, without the use of toxic chemicals. There is no need to hang garments (saving you space) and no additional time involved in carrying out the process when compared with dry cleaning.</p>
      <p style="margin-top:9px">There's a lot to be excited about with Mellowtide, and the fact that it is environmentally friendly is just one of these aspects. The Mellowtide process only uses water (and uses this sparingly) and biodegradable detergents. Not only is this better for our environment, but better for the health of staff using the system. Garments smell fresh and clean, with no toxic fumes.</p>
      <p style="margin-top:9px">What's more, it's completely versatile. A Veltro Mellowtide system can be used for dry cleanable garments as well as commercial laundry. Simply set the machines program to clean a load of woollens, silks or the most delicate of wedding dresses and on the next load select the program for regular laundry such as sheets and towels. It's that simple.</p>
    </div>
    <div class="badge-text abs" style="left:59px;top:390px;width:86px">
      <svg class="tick" viewBox="0 0 10 10"><circle cx="5" cy="5" r="4.3" fill="none" stroke="#fff" stroke-width=".9"/><path d="M3 5.2l1.5 1.4L7.2 3.8" fill="none" stroke="#fff" stroke-width="1"/></svg>
      Advanced<br>Wet Cleaning
      <svg class="tick" viewBox="0 0 10 10"><circle cx="5" cy="5" r="4.3" fill="none" stroke="#fff" stroke-width=".9"/><path d="M3 5.2l1.5 1.4L7.2 3.8" fill="none" stroke="#fff" stroke-width="1"/></svg>
      Unrivalled Results
      <svg class="tick" viewBox="0 0 10 10"><circle cx="5" cy="5" r="4.3" fill="none" stroke="#fff" stroke-width=".9"/><path d="M3 5.2l1.5 1.4L7.2 3.8" fill="none" stroke="#fff" stroke-width="1"/></svg>
      Eco Alternative
    </div>
  </div>
</section>

</body>
</html>
```